Beacon Chillworks business card design

We would like a new design for our business card as we have a new logo.
We need generic business card to give our customers with our office details - with the option of making it individualized for each manager

Target Market(s)

Companies and homeowners

Industry/Entity Type

Air Conditioning

Contact Information for Business Card

We are not sure if we want single or double sided it will depend on the design we choose

Colors
33a6d7
0255a3

Requirements
Must have
• Logo
• phone: (08) 8712 4590
• email: beaconserve@frostmail.example
• website: www.beaconchillworks.example.au
• AU61924
• BLD402613
Nice to have
• Address - Shed 5/218 Kestrel Rd, Harbourvale SA 5742

```html
<!DOCTYPE html>
<html lang="en">
<head>
<meta charset="utf-8">
<title>Beacon Chillworks – Business Card</title>
<link rel="stylesheet" href="https://fonts.googleapis.com/css2?family=Roboto:wght@400;500&family=Roboto+Condensed:wght@400;700&display=swap">
<style>
  :root {
    --backdrop: #2c2d2f;
    --card: #1d1e20;
    --brand-light: #33a6d7;
    --brand-dark: #0255a3;
    --text-light: #f2f2f2;
    --divider: #6b6c70;
  }
  * { box-sizing: border-box; margin: 0; padding: 0; }
  html, body {
    width: 1200px; height: 900px; overflow: hidden;
    background: var(--backdrop);
  }
  .sheet {
    width: 1200px; height: 900px;
    display: flex; flex-direction: column; align-items: center; justify-content: center;
    gap: 44px;
  }
  .card {
    width: 660px; height: 384px;
    background: var(--card);
    position: relative;
    box-shadow: 0 10px 30px rgba(0,0,0,.45);
  }
  /* Front */
  .card--front {
    display: flex; flex-direction: column; align-items: center; justify-content: center;
    gap: 42px;
  }
  .brand { display: flex; align-items: center; gap: 16px; }
  .brand__dot {
    width: 34px; height: 34px; border-radius: 50%;
    background: var(--brand-light);
  }
  .brand__name {
    font-family: "Roboto Condensed", sans-serif;
    font-weight: 700; font-size: 58px;
    color: var(--brand-dark);
    letter-spacing: .5px;
    white-space: nowrap;
  }
  .front__web {
    font-family: "Roboto", sans-serif;
    font-size: 15px; letter-spacing: 4px;
    color: var(--text-light);
  }
  /* Back */
  .person {
    position: absolute; right: 380px; top: 116px;
    text-align: right; white-space: nowrap;
    font-family: "Roboto Condensed", sans-serif;
  }
  .person__name {
    font-weight: 700; font-size: 36px; color: var(--brand-dark);
    text-transform: uppercase; line-height: 1.05;
  }
  .person__role {
    font-weight: 400; font-size: 20px; color: var(--brand-light);
    text-transform: uppercase; margin-top: 2px;
  }
  .divider {
    position: absolute; left: 300px; top: 104px;
    width: 1px; height: 96px; background: var(--divider);
  }
  .contacts {
    position: absolute; left: 322px; top: 112px;
    list-style: none; white-space: nowrap;
    font-family: "Roboto", sans-serif; font-size: 17px; color: var(--text-light);
  }
  .contacts li { display: flex; align-items: center; gap: 10px; height: 26px; }
  .icon { width: 15px; height: 15px; fill: var(--brand-dark); flex: none; }
  .address {
    position: absolute; left: 0; right: 0; top: 258px;
    text-align: center;
    font-family: "Roboto", sans-serif; font-size: 17px; line-height: 1.45;
    color: var(--text-light);
  }
  .address__line { display: inline-flex; align-items: center; gap: 8px; }
</style>
</head>
<body>
<main class="sheet">
  <section class="card card--front" aria-label="Card front">
    <div class="brand">
      <span class="brand__dot"></span>
      <span class="brand__name">Beacon Chillworks</span>
    </div>
    <p class="front__web">www.beaconchillworks.example.au</p>
  </section>

  <section class="card card--back" aria-label="Card back">
    <div class="person">
      <p class="person__name">Daniel Hartley</p>
      <p class="person__role">CEO/Founder</p>
    </div>
    <span class="divider"></span>
    <ul class="contacts">
      <li>
        <svg class="icon" viewBox="0 0 24 24"><path d="M6.6 10.8a15.1 15.1 0 0 0 6.6 6.6l2.2-2.2a1 1 0 0 1 1-.25 11.4 11.4 0 0 0 3.6.57 1 1 0 0 1 1 1V20a1 1 0 0 1-1 1A17 17 0 0 1 3 4a1 1 0 0 1 1-1h3.5a1 1 0 0 1 1 1c0 1.25.2 2.45.57 3.57a1 1 0 0 1-.25 1z"/></svg>
        (08) 8712 4590
      </li>
      <li>
        <svg class="icon" viewBox="0 0 24 24"><path d="M2 5h20v14H2z"/><path d="M2 5l10 8 10-8" fill="none" stroke="#1d1e20" stroke-width="2"/></svg>
        beaconserve@frostmail.example
      </li>
      <li>
        <svg class="icon" viewBox="0 0 24 24"><circle cx="12" cy="12" r="10"/><path d="M2 12h20M12 2c3 3 3 17 0 20M12 2c-3 3-3 17 0 20" fill="none" stroke="#1d1e20" stroke-width="1.6"/></svg>
        beaconchillworks.example.au
      </li>
    </ul>
    <div class="address">
      <span class="address__line">
        <svg class="icon" viewBox="0 0 24 24"><path d="M12 2a7 7 0 0 0-7 7c0 5.2 7 13 7 13s7-7.8 7-13a7 7 0 0 0-7-7zm0 9.5A2.5 2.5 0 1 1 12 6.5a2.5 2.5 0 0 1 0 5z"/></svg>
        Shed 5/218 Kestrel Rd, Harbourvale SA 5742
      </span><br>
      AU61924 | BLD402613
    </div>
  </section>
</main>
</body>
</html>
```